Upscale business cards needed for family business

We need professional business cards created for several family members. We are a family business holding company. We would like these relatively simple and straightforward, but also with a unique element to set them apart. Probably stick with neutral and simple colors - white, grey etc. We need space for the traditional elements, including name, title, address, email/phone number. And we will be creating several from this template so it needs to be template that is easy to switch information in and out of.

Industry/Entity Type

Business

Contact Information for Business Card

Please include the attached Marwood Capital logo.

Requirements
Must have
• The attached Marwood Capital logo.

```html
<!DOCTYPE html>
<html lang="en">
<head>
<meta charset="utf-8">
<title>Marwood Capital – Business Cards</title>
<link rel="stylesheet" href="https://fonts.googleapis.com/css2?family=EB+Garamond:wght@400;500;600&display=swap">
<style>
  :root {
    --backdrop: #2a2a2a;
    --card-black: #151515;
    --card-black-edge: #222222;
    --card-white: #f7f7f5;
    --gold: #c19a3e;
    --gold-light: #dcbf6d;
    --gold-dark: #9a7826;
    --ink: #1c1c1c;
    --silver: #d9d9d9;
  }
  * { margin: 0; padding: 0; box-sizing: border-box; }
  html, body { width: 1200px; height: 873px; overflow: hidden; }
  body {
    background: var(--backdrop);
    font-family: "EB Garamond", Georgia, serif;
    position: relative;
  }
  .card {
    position: absolute;
    top: 288px;
    width: 520px;
    height: 298px;
    box-shadow: 0 10px 30px rgba(0,0,0,.45);
    overflow: hidden;
  }
  /* Front */
  .card-front {
    left: 50px;
    background: linear-gradient(135deg, var(--card-black-edge), var(--card-black));
  }
  .card-front .wordmark {
    position: absolute;
    top: 104px; left: 0; right: 0;
    text-align: center;
    font-size: 38px;
    font-weight: 500;
    letter-spacing: 2px;
    text-transform: uppercase;
    color: var(--silver);
  }
  .card-front .rule {
    position: absolute;
    top: 160px; left: 90px; right: 90px;
    height: 1px;
    background: var(--gold);
  }
  .card-front .web {
    position: absolute;
    top: 214px; left: 0; right: 0;
    text-align: center;
    font-size: 15px;
    letter-spacing: 3px;
    color: var(--gold);
  }
  /* Back */
  .card-back {
    left: 630px;
    background: var(--card-white);
  }
  .card-back .wordmark {
    position: absolute;
    top: 40px; left: 0; right: 0;
    text-align: center;
    font-size: 27px;
    font-weight: 500;
    letter-spacing: 1.5px;
    text-transform: uppercase;
    color: var(--ink);
  }
  .card-back .rule {
    position: absolute;
    top: 82px; left: 150px; right: 150px;
    height: 1px;
    background: var(--gold);
  }
  .holder {
    position: absolute;
    top: 140px; left: 30px;
    width: 190px;
    text-align: right;
  }
  .holder-name {
    font-size: 20px;
    font-weight: 600;
    color: var(--gold);
  }
  .holder-title {
    font-size: 14px;
    color: var(--ink);
  }
  .divider {
    position: absolute;
    top: 112px; left: 244px;
    width: 2px; height: 96px;
    background: linear-gradient(to bottom, transparent, var(--gold), transparent);
  }
  .contacts {
    position: absolute;
    top: 112px; left: 266px;
    list-style: none;
  }
  .contacts li {
    display: flex;
    align-items: center;
    gap: 12px;
    height: 30px;
    font-size: 14.5px;
    color: var(--ink);
  }
  .contacts svg { width: 16px; height: 16px; flex: none; }
  .tagline-band {
    position: absolute;
    left: 0; right: 0; bottom: 0;
    height: 52px;
    background: linear-gradient(to bottom, var(--gold-light), var(--gold) 45%, var(--gold-dark));
    display: flex;
    align-items: center;
    justify-content: center;
  }
  .tagline {
    font-size: 15px;
    font-weight: 600;
    letter-spacing: 4px;
    color: var(--ink);
  }
</style>
</head>
<body>
  <section class="card card-front" aria-label="Card front">
    <div class="wordmark">Marwood Capital</div>
    <div class="rule"></div>
    <div class="web">www.marwoodcapital.com</div>
  </section>

  <section class="card card-back" aria-label="Card back">
    <div class="wordmark">Marwood Capital</div>
    <div class="rule"></div>

    <div class="holder">
      <div class="holder-name">Daniel Varga</div>
      <div class="holder-title">Principal Consultant</div>
    </div>

    <div class="divider"></div>

    <ul class="contacts">
      <li>
        <svg viewBox="0 0 16 16" aria-hidden="true"><path fill="var(--gold)" d="M2 6c0-2 2-3 6-3s6 1 6 3l-2 1-1-2H5L4 7 2 6zm2 2h8l1 5H3l1-5zm4 1.5a1.5 1.5 0 1 0 0 3 1.5 1.5 0 0 0 0-3z"/></svg>
        (+234) 555 0142
      </li>
      <li>
        <svg viewBox="0 0 16 16" aria-hidden="true"><rect x="4.5" y="1" width="7" height="14" rx="1.5" fill="none" stroke="var(--gold)" stroke-width="1.4"/><circle cx="8" cy="12.5" r=".9" fill="var(--gold)"/></svg>
        +61 400 555 018
      </li>
      <li>
        <svg viewBox="0 0 16 16" aria-hidden="true"><rect x="1" y="3" width="14" height="10" fill="var(--gold)"/><path d="M1 3l7 6 7-6" fill="none" stroke="var(--card-white)" stroke-width="1.2"/></svg>
        enquiries@marwoodcapital.com
      </li>
    </ul>

    <div class="tagline-band">
      <span class="tagline">Supporting Lasting Growth</span>
    </div>
  </section>
</body>
</html>
```